BrinTack Holdings Ltd

I'd like to create a company letterhead for the attached logo in word format.

I'd like to emphasis the icon in large translucent state from the left corner and ensure that the letterhead colouring matches the colour palette of the current logo with a contrast so it's clear to see. I've attached a copy of our sister company page on the app for reference.

```html
<!DOCTYPE html>
<html lang="en">
<head>
<meta charset="utf-8">
<title>BrinTack Holdings Ltd — Letterhead</title>
<link rel="stylesheet" href="https://fonts.googleapis.com/css2?family=Nunito:wght@400&display=swap">
<style>
  :root {
    --backdrop: #686b70;
    --paper: #f2f2f2;
    --brand-teal: #4bb8a9;
    --brand-teal-faint: #dce8e6;
    --ink: #4a4d52;
  }
  html, body {
    margin: 0;
    padding: 0;
    width: 1200px;
    height: 803px;
    overflow: hidden;
    background: var(--backdrop);
    font-family: "Nunito", sans-serif;
  }
  .letterhead {
    position: absolute;
    left: 331px;
    top: 21px;
    width: 538px;
    height: 760px;
    background: linear-gradient(135deg, #f6f6f6 0%, var(--paper) 45%, #ececec 75%, #f4f4f4 100%);
    overflow: hidden;
  }
  .corner-emblem {
    position: absolute;
    left: -50px;
    top: 390px;
    width: 388px;
    height: 388px;
    border-radius: 50%;
    background: var(--brand-teal-faint);
    opacity: 0.85;
  }
  .brand {
    position: absolute;
    left: 51px;
    top: 46px;
    display: flex;
    align-items: center;
    gap: 8px;
  }
  .brand-dot {
    width: 34px;
    height: 34px;
    border-radius: 50%;
    background: var(--brand-teal);
  }
  .brand-name {
    color: var(--brand-teal);
    font-size: 19px;
    font-weight: 400;
    letter-spacing: 0.2px;
  }
  .address, .contact {
    position: absolute;
    top: 58px;
    margin: 0;
    color: var(--ink);
    font-size: 8.3px;
    line-height: 12.2px;
    font-style: normal;
  }
  .address { left: 332px; }
  .contact {
    left: 424px;
    list-style: none;
    padding: 0;
  }
  .contact li {
    display: flex;
    align-items: center;
    gap: 6px;
  }
  .contact svg {
    width: 7px;
    height: 7px;
    flex: none;
  }
  .icon-fill { fill: var(--brand-teal); }
  .icon-line { fill: none; stroke: var(--brand-teal); stroke-width: 1; }
  .footer-wave {
    position: absolute;
    left: 0;
    bottom: 0;
    width: 538px;
    height: 40px;
  }
  .footer-wave path { fill: var(--brand-teal); }
</style>
</head>
<body>
  <main class="letterhead">
    <div class="corner-emblem" aria-hidden="true"></div>
    <header>
      <div class="brand">
        <span class="brand-dot"></span>
        <span class="brand-name">BrinTack Holdings Ltd</span>
      </div>
      <address class="address">
        412 Harlow Street<br>
        Suite 220<br>
        Denver, CO 80214
      </address>
      <ul class="contact">
        <li>
          <svg viewBox="0 0 10 10" aria-hidden="true"><path class="icon-fill" d="M2 0.5 L3.6 2.6 L2.8 3.7 C3.4 5 4.8 6.4 6.2 7 L7.3 6.2 L9.5 7.8 L8.4 9.5 C4.5 9.3 0.7 5.5 0.5 1.6 Z"/></svg>
          303-555-0148
        </li>
        <li>
          <svg viewBox="0 0 10 10" aria-hidden="true"><rect class="icon-line" x="0.8" y="2" width="8.4" height="6"/><path class="icon-line" d="M0.8 2 L5 5.3 L9.2 2"/></svg>
          info@brintack.com
        </li>
        <li>
          <svg viewBox="0 0 10 10" aria-hidden="true"><circle class="icon-line" cx="5" cy="5" r="4.3"/><path class="icon-line" stroke-width="0.8" d="M0.8 5 H9.2 M5 0.7 C2.8 3 2.8 7 5 9.3 M5 0.7 C7.2 3 7.2 7 5 9.3"/></svg>
          brintack.com
        </li>
      </ul>
    </header>
    <svg class="footer-wave" viewBox="0 0 538 40" preserveAspectRatio="none" aria-hidden="true">
      <path d="M0 18 C60 28 120 32 200 28 C300 22 420 2 538 6 L538 40 L0 40 Z"/>
    </svg>
  </main>
</body>
</html>
```